Fairhollow Terrace
A PLACE TO CALL YOUR OWN
Professional
Delphine Marquist
Administrator
812 Quillon Avenue
Larkmere,SD 57099
delphine.marquist@fairhollowterrace.org
www.fairhollowterrace.org
Here is the AI file.

```html
<!DOCTYPE html>
<html lang="en">
<head>
<meta charset="utf-8">
<title>Fairhollow Terrace – Business Card</title>
<link rel="stylesheet" href="https://fonts.googleapis.com/css2?family=Cinzel:wght@500&family=Tinos:wght@400;700&display=swap">
<style>
  :root {
    --brown: #6a4a2f;
    --brown-dark: #4f3420;
    --brown-light: #8b6644;
    --ink: #2b1d12;
    --paper: #ffffff;
  }
  * { margin: 0; padding: 0; box-sizing: border-box; }
  html, body {
    width: 1200px;
    height: 686px;
    overflow: hidden;
    background: var(--paper);
  }
  .card {
    position: relative;
    width: 1200px;
    height: 686px;
    background: var(--paper);
    font-family: "Tinos", "Times New Roman", serif;
    color: var(--ink);
    text-align: center;
  }
  .top-band {
    position: absolute;
    top: 0; left: 0;
    width: 100%;
    height: 115px;
    background: linear-gradient(90deg, var(--brown-dark) 0%, var(--brown-light) 50%, var(--brown-dark) 100%);
  }
  .brand-dot {
    position: absolute;
    top: 96px;
    left: 535px;
    width: 130px;
    height: 130px;
    border-radius: 50%;
    background: var(--brown);
    border: 6px solid var(--paper);
  }
  .brand-name {
    position: absolute;
    top: 256px;
    left: 0;
    width: 100%;
    font-family: "Cinzel", "Trajan Pro", serif;
    font-weight: 500;
    font-size: 54px;
    line-height: 64px;
    letter-spacing: 3px;
    color: var(--brown);
    text-transform: uppercase;
  }
  .tagline {
    position: absolute;
    top: 346px;
    left: 360px;
    width: 480px;
    padding-top: 9px;
    border-top: 2px solid var(--brown);
    font-size: 17px;
    line-height: 20px;
    letter-spacing: 5px;
    color: var(--brown);
  }
  .person-name {
    position: absolute;
    top: 430px;
    left: 0;
    width: 100%;
    font-weight: 700;
    font-size: 34px;
    line-height: 42px;
    color: var(--brown-dark);
  }
  .person-title {
    position: absolute;
    top: 478px;
    left: 0;
    width: 100%;
    font-size: 34px;
    line-height: 42px;
    color: var(--ink);
  }
  .contact {
    position: absolute;
    top: 574px;
    left: 0;
    width: 100%;
    font-size: 26px;
    line-height: 37px;
    color: var(--ink);
    white-space: nowrap;
  }
</style>
</head>
<body>
  <div class="card">
    <div class="top-band"></div>
    <span class="brand-dot"></span>
    <div class="brand-name">Fairhollow Terrace</div>
    <div class="tagline">A PLACE TO CALL YOUR OWN</div>
    <div class="person-name">Delphine Marquist</div>
    <div class="person-title">Administrator</div>
    <div class="contact">
      <div class="contact-line">812 Quillon Avenue Larkmere,SD 57099 Phone : (605) 555-0148</div>
      <div class="contact-line">Email : delphine.marquist@fairhollowterrace.org&nbsp; Web : www.fairhollowterrace.org</div>
    </div>
  </div>
</body>
</html>
```